Veltrane Hand Sanitiser Spray Product Range for International Markets

Veltrane is a new Healthcare business launching a full product range of Anti-bacterial Hand Sanitiser Spray bottles in various sizes. We have a new logo which we believe differentiates us from the competition: Veltrane - Care That Goes Further
The Product Range will comprise two distinct product solution types:
- Anti-bacterial Hand Sanitisers - Alcohol based
- Anti-bacterial Hand Sanitisers - Sensitive Non Alcohol based
Bottle sizes will comprise a range containing:
100ml, 250ml, 500ml, 1ltr, 5ltr, 10ltr
Some bottles will have Pump Sprays
The Product labelling will be attractive front packaging label combined with strong product attributes and usage indicator cues.
As a Healthcare brand our logo design is light Green. We believe that this should be combined with blues and greens balanced to create contrast and strong stand-out on-shelf.
A review of competitor brands will show some similar colour cues, however as a Healthcare brand, the colour cues Green and White are synonymous with the sector. Many existing brands are very pragmatic in their label design. i.e. #it does what is says on the tin approach#. Our brand will need strong stand-out and strong aesthetic appeal too, since it will often be left in public view and around the home and office and therefore should look as attractive as possible. There will be other brand variants in the future and thought should be given to this too - with use of colour cues.
For Competitor indicators check-out the brands on Brisklot - Pine Hollow, Dermavell and others....Thank-you!

Target Market(s)

First: Female 25 - 65
Second: Male 25 - 65

Contact Information for Business Card

Garth L. Dunmore
CEO
Veltrane Healthcare Worldwide
'Care That Goes Further'
www.VeltraneHealthcare.example
E. gldunmore@veltranehealthcare.example
T. +44 7700 900318
T. +44 118 496072

Font styles to use
Sans Serif

Colors
34a7d7
33b8a4
add136
fbee3e
b768aa

```html
<!DOCTYPE html>
<html lang="en">
<head>
<meta charset="utf-8">
<title>Veltrane Hand Sanitiser Label</title>
<link rel="stylesheet" href="https://fonts.googleapis.com/css2?family=Poppins:wght@400;500;600;700&family=Roboto+Condensed:wght@300;400&display=swap">
<style>
  :root {
    --backdrop-light: #f7f7f7;
    --backdrop-dark: #dedede;
    --label-white: #ffffff;
    --brand-green: #3cb54a;
    --lime: #8dc63f;
    --lime-bright: #b5d334;
    --body-green-top: #3bb54a;
    --body-green-mid: #27b374;
    --body-teal: #44c3a8;
    --label-edge: #d4d4d4;
  }
  html, body {
    margin: 0;
    padding: 0;
    overflow: hidden;
  }
  .canvas {
    width: 1200px;
    height: 1200px;
    overflow: hidden;
    background: radial-gradient(ellipse at 50% 30%, var(--backdrop-light) 0%, var(--backdrop-light) 45%, var(--backdrop-dark) 100%);
    display: flex;
    align-items: center;
    justify-content: center;
  }
  .product-label {
    width: 600px;
    height: 923px;
    display: block;
    outline: 1px solid var(--label-edge);
    box-shadow: 0 6px 24px rgba(0,0,0,0.08);
  }
  .brand-name {
    font-family: "Poppins", sans-serif;
    font-weight: 500;
    fill: var(--brand-green);
  }
  .product-type {
    font-family: "Poppins", sans-serif;
    font-weight: 400;
    fill: var(--label-white);
    letter-spacing: 0.6px;
  }
  .product-type .strong { font-weight: 700; }
  .product-name {
    font-family: "Roboto Condensed", sans-serif;
    font-weight: 400;
    fill: var(--label-white);
  }
  .formula-tag {
    font-family: "Poppins", sans-serif;
    font-weight: 500;
    fill: var(--body-green-mid);
  }
  .claim-title {
    font-family: "Poppins", sans-serif;
    font-weight: 700;
    fill: var(--label-white);
  }
  .claim-detail {
    font-family: "Poppins", sans-serif;
    font-weight: 600;
    fill: var(--label-white);
  }
  .volume {
    font-family: "Roboto Condensed", sans-serif;
    font-weight: 400;
    fill: var(--label-white);
  }
  .usage-ring-text {
    font-family: "Poppins", sans-serif;
    font-weight: 500;
    fill: var(--label-white);
    letter-spacing: 0.4px;
  }
</style>
</head>
<body>
<main class="canvas">
  <svg class="product-label" viewBox="0 0 262 403" xmlns="http://www.w3.org/2000/svg" aria-label="Veltrane antibacterial hand sanitizer label">
    <defs>
      <linearGradient id="bodyGradient" x1="0" y1="0" x2="0" y2="1">
        <stop offset="0" stop-color="var(--body-green-top)"/>
        <stop offset="0.5" stop-color="var(--body-green-mid)"/>
        <stop offset="1" stop-color="var(--body-teal)"/>
      </linearGradient>
      <linearGradient id="limeGradient" x1="0" y1="0" x2="1" y2="0">
        <stop offset="0" stop-color="var(--lime)"/>
        <stop offset="1" stop-color="var(--lime-bright)"/>
      </linearGradient>
      <path id="usageArc" d="M199.5,373.6 A33,33 0 1 1 244.6,328.5"/>
    </defs>

    <rect class="label-base" x="0" y="0" width="262" height="403" fill="var(--label-white)"/>

    <g class="brand-block">
      <text class="brand-name" x="131" y="76" text-anchor="middle" font-size="24">Veltrane</text>
    </g>

    <path class="lime-swoosh" d="M0,158 C100,156 205,122 262,56 L262,70 C205,132 100,168 0,171 Z" fill="url(#limeGradient)"/>
    <path class="body-panel" d="M0,176 C105,173 212,140 262,78 L262,403 L0,403 Z" fill="url(#bodyGradient)"/>

    <text class="product-type" x="131" y="214" text-anchor="middle" font-size="9.5"><tspan class="strong">ANTI</tspan>BACTERIAL</text>
    <text class="product-name" x="131" y="245" text-anchor="middle" font-size="27">HAND SANITIZER</text>
    <rect class="formula-pill" x="70" y="252" width="122" height="15" rx="3" fill="var(--label-white)"/>
    <text class="formula-tag" x="131" y="262.5" text-anchor="middle" font-size="7">NON-ALCOHOL BASED</text>

    <text class="claim-title" x="31" y="318" font-size="8.5">KILLS 99.9%</text>
    <line class="claim-rule" x1="31" y1="323" x2="98" y2="323" stroke="var(--label-white)" stroke-width="1"/>
    <text class="claim-detail" x="31" y="336" font-size="5.4">VIRUSES, GERMS</text>
    <text class="claim-detail" x="31" y="343" font-size="5.4">AND BACTERIA</text>

    <g class="usage-badge">
      <text class="usage-ring-text" font-size="6"><textPath href="#usageArc">FOR HANDS SKIN AND SURFACES</textPath></text>
      <g role="img" aria-label="Icon of an open hand with water drops falling onto it">
        <circle cx="216" cy="345" r="18" fill="var(--label-white)" fill-opacity="0.22"/>
      </g>
    </g>

    <text class="volume" x="31" y="378" font-size="9">500ml / 16.9 US Fl. Oz</text>
  </svg>
</main>
</body>
</html>
```